Business card for Sports Apparel business

DOUBLE SIDED DESIGN
We need business cards for a new sports apparel business. We are developing a protective headband for soccer initially.
Quorvane is focused on designing and developing head protection products to reduce the likelihood of concussion when playing sports. Exploring and understanding medical insights, material science research, current and former players experiences and governing bodies guidelines has allowed Quorvane to develop the safety, style, form and function requirements of a suitable product to bring to market.
Target Market(s)
Mums buying kits for the sons and daughters. Amateur footballers.
Industry/Entity Type
Sporting Good
Contact Information for Business Card
Martin Ellwood - CEO
Mobile: +44 7700123456
Email: martin@quorvane.co.uk
Tel: 0208 1234567
Rosalind Pyke - COO
Mob: +44 7700 654321
Email: rosalind@quorvane.co.uk
Tel: 0208 1234567
Gordon Haley - CCO
Mob: +44 7700 987654
Email: gordon@quorvane.co.uk
Tel: 0208 1234567
Look and feel
Each slider illustrates characteristics of the customer's brand and the style your logo design should communicate.

```html
<!DOCTYPE html>
<html lang="en">
<head>
<meta charset="utf-8">
<title>Quorvane Business Card</title>
<link href="https://fonts.googleapis.com/css2?family=Open+Sans:wght@400;600;700&display=swap" rel="stylesheet">
<style>
  :root {
    --page-bg: #e9eaec;
    --card-white: #f7f7f5;
    --brand-blue: #0c56a0;
    --rule-grey: #5a5a5a;
    --ink-dark: #4a4a4a;
    --ink-light: #ffffff;
  }
  html, body {
    margin: 0;
    padding: 0;
    width: 1200px;
    height: 1116px;
    overflow: hidden;
    background: var(--page-bg);
    font-family: "Open Sans", Arial, sans-serif;
  }
  .business-card {
    position: absolute;
    left: 100px;
    top: 234px;
    width: 1000px;
    height: 647px;
    background: var(--card-white);
    box-shadow: 0 18px 40px rgba(0,0,0,0.18);
    overflow: hidden;
  }
  .brand-area {
    position: absolute;
    left: 0; top: 0;
    width: 100%;
    height: 318px;
  }
  .brand-name {
    position: absolute;
    left: 190px;
    top: 140px;
    margin: 0;
    font-size: 92px;
    font-weight: 600;
    letter-spacing: 4px;
    color: var(--ink-dark);
    line-height: 1;
  }
  .divider-rule {
    position: absolute;
    left: 0; top: 318px;
    width: 100%;
    height: 10px;
    background: var(--rule-grey);
  }
  .info-band {
    position: absolute;
    left: 0; top: 328px;
    width: 100%;
    height: 319px;
    background: var(--brand-blue);
    color: var(--ink-light);
  }
  .contact-list {
    position: absolute;
    left: 545px;
    top: 36px;
    margin: 0;
    padding: 0;
    list-style: none;
  }
  .contact-item {
    display: flex;
    align-items: center;
    gap: 16px;
    font-size: 30px;
    line-height: 1;
    height: 50px;
    white-space: nowrap;
  }
  .contact-icon {
    width: 30px;
    height: 30px;
    flex: none;
  }
  .person {
    position: absolute;
    left: 70px;
    bottom: 40px;
    margin: 0;
    font-size: 40px;
    display: flex;
    align-items: center;
    white-space: nowrap;
  }
  .person-name {
    font-weight: 700;
    letter-spacing: 0.5px;
  }
  .person-sep {
    display: inline-block;
    width: 2px;
    height: 44px;
    background: var(--ink-light);
    margin: 0 14px;
  }
  .person-role {
    font-weight: 400;
  }
</style>
</head>
<body>
  <div class="business-card">
    <div class="brand-area">
      <p class="brand-name">QUORVANE</p>
    </div>
    <div class="divider-rule"></div>
    <div class="info-band">
      <ul class="contact-list">
        <li class="contact-item">
          <svg class="contact-icon" viewBox="0 0 30 30" aria-hidden="true">
            <circle cx="15" cy="15" r="15" fill="#fff"/>
            <rect x="10.5" y="7" width="9" height="16" rx="1.5" fill="none" stroke="#0c56a0" stroke-width="1.6"/>
            <circle cx="15" cy="20.5" r="0.9" fill="#0c56a0"/>
          </svg>
          <span>+44 7700123456</span>
        </li>
        <li class="contact-item">
          <svg class="contact-icon" viewBox="0 0 30 30" aria-hidden="true">
            <circle cx="15" cy="15" r="15" fill="#fff"/>
            <rect x="7.5" y="10" width="15" height="10.5" fill="none" stroke="#0c56a0" stroke-width="1.6"/>
            <polyline points="7.5,10 15,16 22.5,10" fill="none" stroke="#0c56a0" stroke-width="1.6"/>
          </svg>
          <span>martin@quorvane.co.uk</span>
        </li>
        <li class="contact-item">
          <svg class="contact-icon" viewBox="0 0 30 30" aria-hidden="true">
            <circle cx="15" cy="15" r="15" fill="#fff"/>
            <path d="M11 8.5 l3 3 -1.6 2 c0.9 1.8 2.3 3.2 4.1 4.1 l2-1.6 3 3 -1.8 2.2 c-5.4 -0.6 -9.4 -4.6 -10 -10 z" fill="#0c56a0"/>
          </svg>
          <span>0208 1234567</span>
        </li>
      </ul>
      <p class="person">
        <span class="person-name">MARTIN ELLWOOD</span>
        <span class="person-sep"></span>
        <span class="person-role">CEO</span>
      </p>
    </div>
  </div>
</body>
</html>
```